Redesign our business card for more impact

We want to completely replace the back design of our card, and refresh or even change the front entirely. We are happy with our black Q7 logo and do not want to change it.
Our company address changed too. It is now 58 Corvallen, Irvine, CA 92741
Updates

It was reported by Sketch Harbor email today that the uploaded files didnt upload. I am trying again.

Target Market(s)

Architects and Building Owners (People making multi-million dollar decisions)

Industry/Entity Type

Consulting Engineering

Contact Information for Business Card

Contact info on the front. "wallpaper" design on back with tag line on the back "Engineering Your Future"

Font styles to use
Sans Serif

Requirements
Must have
• A vivid, modern, impactful ...but tasteful back of card design. It should communicate our premier status, but grab attention as innovative. DESIGN SHOULD BE ELEGANT AND NOT TOO BUSY.
Nice to have
• Repeating pattern, multi-color, something creative...
Should not have
• Anything that looks too playful or that we are not serious professionals. It should also not be too boring or conservative.

```html
<!DOCTYPE html>
<html lang="en">
<head>
<meta charset="utf-8">
<title>Q7 Engineering Business Card</title>
<link rel="stylesheet" href="https://fonts.googleapis.com/css2?family=Krona+One&family=Poppins:wght@300;400&display=swap">
<style>
  :root {
    --page: #ffffff;
    --ink-white: #ffffff;
    --card-dark: #1e1e1f;
    --text-soft: #e6e6e6;
    --cyan: #19e3f0;
    --violet: #b58cff;
    --pink: #ff5cf5;
    --deep-blue: #4a5cff;
  }
  * { margin: 0; padding: 0; box-sizing: border-box; }
  html, body {
    width: 936px; height: 1200px; overflow: hidden;
    background: var(--page);
  }
  .canvas { position: relative; width: 936px; height: 1200px; }

  .card {
    position: absolute; left: 109px; width: 719px; height: 411px;
    overflow: hidden;
  }
  .card--front {
    top: 156px;
    background:
      radial-gradient(ellipse 30% 28% at 62% 0%, #00ffc8 0%, rgba(0,255,200,0) 100%),
      radial-gradient(ellipse 45% 55% at 80% 18%, #00e4f5 0%, rgba(0,228,245,0) 100%),
      radial-gradient(ellipse 45% 50% at 68% 62%, #10b8ff 0%, rgba(16,184,255,0) 100%),
      radial-gradient(ellipse 40% 45% at 38% 100%, var(--pink) 0%, rgba(255,92,245,0) 100%),
      radial-gradient(ellipse 35% 55% at 8% 50%, #a9a2ff 0%, rgba(169,162,255,0) 100%),
      radial-gradient(ellipse 40% 40% at 100% 90%, #7a55ff 0%, rgba(122,85,255,0) 100%),
      var(--deep-blue);
  }
  .card--back { top: 635px; background: var(--card-dark); }

  .tile-pattern { position: absolute; left: 0; top: 0; width: 719px; height: 411px; }

  .rule-vertical {
    position: absolute; left: 57px; top: 0; width: 1px;
    background: var(--ink-white);
  }
  .card--front .rule-vertical { height: 300px; }
  .card--back .rule-vertical { height: 211px; }
  .rule-horizontal { height: 1px; background: var(--ink-white); }

  .brand-name {
    position: absolute; left: 0; right: 0; top: 78px;
    text-align: center;
    font-family: "Krona One", sans-serif;
    font-size: 128px; line-height: 1;
    color: var(--ink-white);
  }
  .tagline {
    position: absolute; left: 55px; top: 312px;
    font-family: "Krona One", sans-serif;
    font-size: 20px; line-height: 30px;
    color: var(--ink-white);
  }
  .front-rule { position: absolute; left: 291px; top: 362px; width: 210px; }
  .front-url {
    position: absolute; left: 518px; top: 347px;
    font-family: "Poppins", sans-serif; font-size: 17px;
    color: var(--ink-white);
  }

  .person-name {
    position: absolute; left: 79px; top: 60px;
    font-family: "Krona One", sans-serif;
    font-size: 23px; line-height: 25px; font-weight: 400;
    background: linear-gradient(90deg, var(--cyan) 0%, #43a8ff 55%, var(--violet) 100%);
    -webkit-background-clip: text; background-clip: text;
    color: transparent;
  }
  .credentials {
    position: absolute; left: 79px; top: 118px;
    font-family: "Poppins", sans-serif; font-weight: 300;
    font-size: 17px; line-height: 26px; color: var(--text-soft);
  }
  .contact-list {
    position: absolute; left: 55px; top: 219px; list-style: none;
    font-family: "Poppins", sans-serif; font-weight: 300;
    font-size: 18.5px; line-height: 26px; color: var(--text-soft);
  }
  .contact-list li { display: flex; align-items: center; gap: 9px; }
  .contact-icon { width: 16px; height: 16px; flex: none; }
  .address-row {
    position: absolute; left: 55px; top: 335px;
    display: flex; align-items: center; gap: 16px;
  }
  .address {
    font-family: "Poppins", sans-serif; font-size: 16px; white-space: nowrap;
    background: linear-gradient(90deg, var(--cyan), var(--violet));
    -webkit-background-clip: text; background-clip: text;
    color: transparent;
  }
  .address-row .rule-horizontal { width: 230px; }
</style>
</head>
<body>
<div class="canvas">

  <section class="card card--front">
    <svg class="tile-pattern" viewBox="0 0 719 411" role="img" aria-label="Faint repeating tile pattern">
      <g fill="#ffffff" opacity="0.1">
        <polygon points="617,69 722,69 702,137 597,137"/>
        <polygon points="685,137 740,137 720,206 665,206"/>
        <polygon points="581,206 685,206 665,274 561,274"/>
        <polygon points="650,274 740,274 720,340 630,340"/>
      </g>
    </svg>
    <div class="rule-vertical"></div>
    <div class="brand-name">Q7</div>
    <p class="tagline">Engineering<br>Your Future</p>
    <div class="rule-horizontal front-rule"></div>
    <span class="front-url">www.q7eng.com</span>
  </section>

  <section class="card card--back">
    <svg class="tile-pattern" viewBox="0 0 719 411" role="img" aria-label="Repeating tile pattern in cyan to violet gradient">
      <defs>
        <linearGradient id="pg" gradientUnits="userSpaceOnUse" x1="0" y1="0" x2="0" y2="411">
          <stop offset="0" stop-color="#00f0f0"/>
          <stop offset="0.5" stop-color="#1b8dff"/>
          <stop offset="1" stop-color="#5a4dff"/>
        </linearGradient>
      </defs>
      <g fill="url(#pg)">
        <polygon points="722,0 740,0 720,69 702,69"/>
        <polygon points="617,69 722,69 702,137 597,137"/>
        <polygon points="685,137 740,137 720,206 665,206"/>
        <polygon points="581,206 685,206 665,274 561,274"/>
        <polygon points="650,274 740,274 720,340 630,340"/>
        <polygon points="545,340 650,340 630,411 525,411"/>
      </g>
    </svg>
    <div class="rule-vertical"></div>
    <h1 class="person-name">DARIN<br>WHITFIELD, PE</h1>
    <p class="credentials">HFDP, LEED AP<br>CEO/Principal</p>
    <ul class="contact-list">
      <li>
        <svg class="contact-icon" viewBox="0 0 16 16"><defs><linearGradient id="ig" x1="0" y1="0" x2="1" y2="1"><stop offset="0" stop-color="#19e3f0"/><stop offset="1" stop-color="#b58cff"/></linearGradient></defs><path d="M3.5 1.5l2.2 2.6-1.3 1.8c.9 2 2.6 3.7 4.6 4.6l1.8-1.3 2.6 2.2-1.4 2.1C7 13 3 9 1.5 2.9z" fill="url(#ig)"/></svg>
        (555) 014-2270
      </li>
      <li>
        <svg class="contact-icon" viewBox="0 0 16 16"><rect x="1" y="3.5" width="14" height="9.5" fill="url(#ig)"/><path d="M1 3.5l7 5.5 7-5.5" stroke="#1e1e1f" stroke-width="1.2" fill="none"/></svg>
        darin.whitfield@q7eng.com
      </li>
      <li>
        <svg class="contact-icon" viewBox="0 0 16 16"><circle cx="8" cy="8" r="6.5" fill="none" stroke="url(#ig)" stroke-width="1.5"/><ellipse cx="8" cy="8" rx="2.8" ry="6.5" fill="none" stroke="url(#ig)" stroke-width="1.2"/><path d="M1.5 8h13" stroke="url(#ig)" stroke-width="1.2"/></svg>
        q7eng.com
      </li>
    </ul>
    <div class="address-row">
      <span class="address">58 Corvallen, Irvine, CA 92741</span>
      <div class="rule-horizontal"></div>
    </div>
  </section>

</div>
</body>
</html>
```